Design of a chocolate packaging

In hand-lettering-style: "Thank you for your work - you are an important part of our team!" (in big letters - almost 2/3 of the whole place) "This chocolate is a lot, so you enter into a raffle and have a great chance of a Zelta Rovo and many more great winnings ... all the information is below www.brv-nordlichtwerk.de! Good luck !!! " (in small letters underneath) The place is: 7,3cm * 15,3cm (crosswise)

Font styles to use
Script

```html
<!DOCTYPE html>
<html lang="de">
<head>
<meta charset="utf-8">
<title>Schokoladenverpackung – Danke für Deine Arbeit</title>
<link rel="stylesheet" href="https://fonts.googleapis.com/css2?family=Kaushan+Script&display=swap">
<style>
  :root {
    --page: #ffffff;
    --red: #e41e26;
    --red-dark: #a8161c;
    --brown: #5c3716;
    --brown-light: #7a4d22;
    --cream: #fff9c8;
    --ink: #1e1a17;
    --paper-white: #ffffff;
    --paper-grey: #b9b9b9;
  }
  * { margin: 0; padding: 0; box-sizing: border-box; }
  html, body {
    width: 1200px; height: 1000px; overflow: hidden;
    background: var(--page);
    font-family: "Kaushan Script", cursive;
  }
  .label {
    position: absolute; left: 180px; width: 840px; height: 400px;
    box-shadow: 10px 12px 14px rgba(0,0,0,0.35);
    overflow: hidden;
  }
  .label--red { top: 73px; }
  .label--brown { top: 518px; }
  .label__art { position: absolute; inset: 0; width: 840px; height: 400px; }
  .headline, .subline, .raffle {
    position: absolute; left: 0; width: 100%;
    text-align: center; white-space: nowrap;
  }
  .headline { font-size: 66px; line-height: 1; }
  .subline { font-size: 39px; line-height: 1; }
  .raffle {
    left: 62px; width: auto; text-align: left;
    font-size: 16.5px; line-height: 31px;
  }
  .label--red .headline, .label--red .subline {
    color: var(--paper-white);
    text-shadow: 3px 4px 4px rgba(0,0,0,0.45);
  }
  .label--red .headline { top: 52px; }
  .label--red .subline { top: 146px; }
  .label--red .raffle { top: 257px; color: var(--ink); }
  .label--brown .headline, .label--brown .subline {
    color: var(--ink);
    text-shadow: 3px 4px 4px rgba(0,0,0,0.35);
  }
  .label--brown .headline { top: 52px; }
  .label--brown .subline { top: 148px; }
  .label--brown .raffle { top: 278px; left: 58px; color: var(--cream); }
</style>
</head>
<body>

<section class="label label--red">
  <svg class="label__art" viewBox="0 0 840 400" aria-hidden="true">
    <defs>
      <linearGradient id="redGrad" x1="0" y1="0" x2="0" y2="1">
        <stop offset="0" stop-color="var(--red-dark)"/>
        <stop offset="0.25" stop-color="var(--red)"/>
      </linearGradient>
    </defs>
    <rect width="840" height="400" fill="var(--brown)"/>
    <path d="M25,250 L815,250 q-6,15 0,30 t0,30 t0,30 t0,30 L815,368
             q-20,8 -40,0 t-40,0 t-40,0 t-40,0 t-40,0 t-40,0 t-40,0 t-40,0 t-40,0 t-40,0
             t-40,0 t-40,0 t-40,0 t-40,0 t-40,0 t-40,0 t-40,0 t-40,0 t-30,0 Z"
          fill="var(--cream)" style="filter: drop-shadow(4px 5px 4px rgba(0,0,0,0.45))"/>
    <path d="M0,252 L40,246 L90,244 L140,238 L190,236 L240,226 L300,224 L360,220 L420,214 L480,214 L540,210 L600,206 L640,198 L690,204 L740,214 L800,216 L840,222 L840,234 L0,258 Z"
          fill="var(--paper-grey)"/>
    <path d="M0,246 L40,240 L90,238 L140,232 L190,230 L240,220 L300,218 L360,214 L420,208 L480,208 L540,204 L600,200 L640,192 L690,198 L740,208 L800,210 L840,216 L840,226 L0,254 Z"
          fill="var(--paper-white)"/>
    <path d="M0,0 H840 V210 L800,204 L740,202 L690,194 L640,188 L600,196 L540,198 L480,202 L420,202 L360,208 L300,212 L240,214 L190,222 L140,226 L90,232 L40,236 L0,240 Z"
          fill="url(#redGrad)"/>
  </svg>
  <h1 class="headline">Danke für Deine Arbeit</h1>
  <p class="subline">Du bist ein wichtiger Teil unseres Teams!</p>
  <p class="raffle">Diese Schokolade ist ein Los. Du nimmst damit an einer Verlosung Teil und hast großartige<br>
  Chancen auf einen Zelta Rovo und viele weitere tolle Gewinne...alle Infos gibt es unter<br>
  www.brv-nordlichtwerk.de! Viel Glück!!!</p>
</section>

<section class="label label--brown">
  <svg class="label__art" viewBox="0 0 840 400" aria-hidden="true">
    <defs>
      <linearGradient id="brownGrad" x1="0" y1="0" x2="0" y2="1">
        <stop offset="0" stop-color="var(--brown)"/>
        <stop offset="1" stop-color="var(--brown-light)"/>
      </linearGradient>
    </defs>
    <rect width="840" height="400" fill="url(#brownGrad)"/>
    <path d="M25,22 q20,-8 40,0 t40,0 t40,0 t40,0 t40,0 t40,0 t40,0 t40,0 t40,0 t40,0
             t40,0 t40,0 t40,0 t40,0 t40,0 t40,0 t40,0 t40,0 t40,0 t30,0
             q-6,15 0,30 t0,30 t0,30 t0,30 t0,30 t0,30 t0,30 L815,270 L25,270
             q6,-15 0,-30 t0,-30 t0,-30 t0,-30 t0,-30 t0,-30 t0,-30 Z"
          fill="var(--cream)"/>
    <path d="M0,262 C120,225 230,200 330,210 C470,222 560,245 680,250 C760,253 810,250 840,246 V400 H0 Z"
          fill="url(#brownGrad)" style="filter: drop-shadow(0 -3px 3px rgba(0,0,0,0.4))"/>
  </svg>
  <h2 class="headline">Danke für Deine Arbeit</h2>
  <p class="subline">Du bist ein wichtiger Teil unseres Teams!</p>
  <p class="raffle">Diese Schokolade ist ein Los. Du nimmst damit an einer Verlosung Teil und hast großartige<br>
  Chancen auf einen Zelta Rovo und viele weitere tolle Gewinne...alle Infos gibt es unter<br>
  www.brv-nordlichtwerk.de! Viel Glück!!!</p>
</section>

</body>
</html>
```